VLK IT Solutions Provider

Please read attached documentation completely before beginning Project. Thank you!

Folio Nest Project Requirements

Thank you for your interest in this design contest. We are always welcome to questions and are looking forward to seeing what you can come up with.

The logo is located on the current site homepage http://www.vantolirex.com/

Bootstrap

We work on a Bootstrap platform with our custom built CMS. We require all designs to be

sized accordingly with the bootstrap grid system found here: http://trelvanix.com/css/#grid

Start of Competition Requirements

At the start of a competition, we are looking for general Home Page Design concepts and interior page design concepts as well.

HOME PAGE DESIGN

Any changes requested by the client in the original designs

Responsive Tablet View (using standard bootstrap media queries, we need to see an

example of a tablet size home page view)

Responsive Phone View (using standard bootstrap media queries, we need to see an

example of a phone size home page view)

INTERIOR PAGE DESIGN

These pages are general content pages. Our CMS allows for the creation of unlimited

pages and gives the client control of adding them. Interior Page Designs can be built

with 1 column, 2 columns (either right side bar or left sidebar)

Examples of buttons and button states,

Examples of drop down menus

Examples of H1 through H5 plus body copy

We uploaded a clean logo to use on the project. Thank you.

Project Deadline Extended

We added a updated Creative Brief document to help out. Please take a look thanks!

```html
<!DOCTYPE html>
<html lang="en">
<head>
<meta charset="utf-8">
<title>VLK – IT Solutions Provider</title>
<link href="https://fonts.googleapis.com/css2?family=Amaranth:wght@400;700&family=Open+Sans:wght@400;600&family=Noto+Serif:ital@0;1&display=swap" rel="stylesheet">
<style>
:root{
  --blue:#0b4f9c;
  --blue-soft:#3a86c4;
  --yellow:#e9b123;
  --ink:#2b2b2b;
  --muted:#666;
  --line:#e3e3e3;
  --grey-band:#f1f1f1;
  --footer:#363b42;
  --footer-deep:#2b2f35;
  --teal:#1fb8a0;
  --white:#fff;
}
*{margin:0;padding:0;box-sizing:border-box}
html,body{width:746px;height:1200px;overflow:hidden;background:var(--white)}
body{position:relative;font-family:"Open Sans",sans-serif;color:var(--ink)}
.abs{position:absolute}
.heading{font-family:"Amaranth",sans-serif;font-weight:400}

/* top bar */
.topbar{top:0;left:0;width:746px;height:16px;background:#f7f7f7;border-bottom:1px solid var(--line)}
.topbar-links{left:68px;top:3px;font-size:5.5px;color:#777;display:flex;gap:5px}
.topbar-links span+span{border-left:1px solid #ccc;padding-left:5px}
.topbar-social{right:70px;top:2px;display:flex;gap:2px}
.topbar-social i{width:10px;height:10px;background:#c3c3c3;display:block}

/* header */
.brand{left:66px;top:26px;display:flex;align-items:center;gap:5px}
.brand-mark{width:10px;height:10px;background:var(--yellow);border-radius:50%}
.brand-name{font-family:"Amaranth",sans-serif;font-weight:700;font-size:26px;color:var(--blue);line-height:1}
.brand-sub{left:66px;top:50px;font-size:4.8px;font-weight:600;color:var(--blue);letter-spacing:.2px}
.callus{left:572px;top:36px;font-size:7px;color:#888;display:flex;align-items:center;gap:3px}
.header-rule{top:64px;left:0;width:746px;height:1px;background:var(--line)}

/* nav */
.nav{top:66px;left:0;width:746px;height:32px}
.nav-home{left:66px;top:0;width:64px;height:32px;background:var(--blue-soft);color:var(--white);text-align:center;padding-top:9px;font-size:7px;line-height:1}
.nav-home small{display:block;font-size:5px;opacity:.85;margin-top:1px}
.nav-item{top:0;height:32px;line-height:32px;font-size:8px;color:#333}
.nav-sep{top:0;width:1px;height:32px;background:var(--line)}
.nav-search{left:570px;top:8px;width:104px;height:16px;border:1px solid var(--line);font-size:5.5px;color:#999;padding:4px 6px}
.nav-search svg{position:absolute;right:5px;top:4px}

/* hero */
.hero{top:98px;left:0;width:746px;height:264px;background:linear-gradient(100deg,#1c3347 0%,#2c4a60 40%,#4d5f6a 70%,#7a6a55 100%)}
.hero-title{left:70px;top:170px;font-size:22px;color:var(--white);line-height:28px;font-weight:700}
.hero-sub{left:70px;top:232px;font-size:14px;color:var(--white)}
.btn{display:flex;align-items:center;justify-content:center;font-size:9.5px;font-weight:600;color:var(--white)}
.btn-how{left:67px;top:270px;width:107px;height:26px;background:var(--blue)}
.btn-more{left:186px;top:270px;width:108px;height:26px;background:var(--yellow)}
.hero-dots{left:365px;top:342px;display:flex;gap:5px}
.hero-dots i{width:7px;height:7px;border-radius:50%;background:var(--white);display:block}
.hero-dots i:first-child{background:var(--yellow);width:9px;height:9px;margin-top:-1px}

/* features */
.feature{top:384px;width:152px;text-align:center}
.feature-icon{height:42px;display:flex;align-items:flex-end;justify-content:center}
.feature h3{font-family:"Amaranth",sans-serif;font-size:9.5px;font-weight:400;color:#222;margin-top:8px}
.feature p{font-size:6.2px;line-height:11px;color:#333;text-align:left;margin-top:6px}
.features-rule{top:504px;left:0;width:746px;height:1px;background:#ddd}

/* testimonial */
.testimonial{top:505px;left:0;width:746px;height:101px;background:var(--grey-band)}
.avatar{left:84px;top:526px;width:60px;height:60px;border-radius:50%;background:radial-gradient(circle at 50% 40%,#d9b79a,#8a6a55 70%);border:3px solid var(--white);box-shadow:0 0 0 1px #ddd}
.arrow-box{top:549px;width:14px;height:14px;background:#d6d6d6;display:flex;align-items:center;justify-content:center}
.quote{left:158px;top:533px;width:458px;font-family:"Noto Serif",serif;font-size:6.5px;line-height:12px;color:#777}
.quote-author{left:158px;top:566px;font-family:"Noto Serif",serif;font-style:italic;font-size:6.5px;color:#999}

/* about */
.section-title{font-family:"Amaranth",sans-serif;font-weight:400;font-size:11px;color:#222;display:flex;align-items:center;gap:6px}
.about-title{left:72px;top:624px}
.about-rule{left:245px;top:631px;width:193px;height:1px;background:var(--line)}
.about-intro{left:72px;top:651px;width:360px;font-size:6px;line-height:10px;color:#777}
.about-list{left:72px;top:684px;width:406px;list-style:none}
.about-list li{height:23px;border-top:1px solid var(--line);display:flex;align-items:center;font-size:6.2px;color:#555;position:relative}
.about-list li:last-child{border-bottom:1px solid var(--line)}
.about-list .ico{width:11px;height:11px;background:var(--blue-soft);margin:0 8px 0 2px;flex:none}
.about-list .plus{position:absolute;right:4px;top:5px;font-size:11px;color:#bbb;font-weight:300}

/* news */
.news-title{left:495px;top:622px}
.news-arrows{left:653px;top:625px;display:flex;gap:1px}
.news-arrows i{width:9px;height:8px;background:var(--blue-soft);display:block}
.news-image{left:495px;top:646px;width:177px;height:90px;background:linear-gradient(160deg,#f2f2f2,#d8d8d8)}
.news-date{left:496px;top:727px;width:46px;height:9px;background:#2e4a68;color:var(--white);font-size:5px;padding:1px 4px}
.news-type{left:495px;top:743px;font-size:6.5px;color:var(--blue-soft)}
.news-text{left:495px;top:758px;width:180px;font-size:6px;line-height:12px;color:#777}

/* cta */
.cta{top:834px;left:0;width:746px;height:70px;background:var(--grey-band);border-top:1px solid #e6e6e6;border-bottom:1px solid #e6e6e6}
.cta-title{left:67px;top:850px;font-size:16px;color:#222}
.cta-title em{font-style:normal;color:var(--blue)}
.cta-text{left:67px;top:880px;font-size:6px;color:#777}
.btn-cta{left:557px;top:852px;width:114px;height:32px;background:var(--blue-soft);border-radius:2px;font-size:10px;box-shadow:0 1px 0 #2b6a9c}

/* partners */
.partners-title{left:0;top:930px;width:746px;text-align:center;font-size:16px;color:#222}

/* footer */
.footer{top:1068px;left:0;width:746px;height:106px;background:var(--footer)}
.footer-brand{left:62px;top:1084px;display:flex;align-items:center;gap:5px}
.footer-brand .brand-name{color:var(--white)}
.footer-sub{left:64px;top:1108px;font-size:4.8px;font-weight:600;color:var(--white)}
.footer-text{left:66px;top:1130px;width:420px;font-size:6px;line-height:8px;color:#aab}
.newsletter-title{left:521px;top:1088px;font-size:9.5px;color:var(--white);font-family:"Open Sans",sans-serif;font-weight:400}
.newsletter-text{left:521px;top:1104px;width:170px;font-size:5.8px;line-height:7px;color:#aab}
.newsletter-input{left:519px;top:1131px;width:113px;height:21px;background:#2a2e33;border:1px solid #4a5058;font-size:6px;color:#888;padding:6px 8px}
.newsletter-btn{left:632px;top:1131px;width:57px;height:21px;background:var(--teal);font-size:7px}
.bottombar{top:1174px;left:0;width:746px;height:26px;background:var(--footer-deep)}
.copyright{left:66px;top:1182px;font-size:6.5px;color:#ddd}
.bottom-social{left:589px;top:1179px;display:flex;gap:8px}
.bottom-social i{width:14px;height:14px;border-radius:50%;background:#7d838a;display:block}
</style>
</head>
<body>

<!-- top bar -->
<div class="abs topbar"></div>
<div class="abs topbar-links"><span>About Us</span><span>Contact Us</span><span>&#9906; Search</span><span>&#9679; English &#711;</span></div>
<div class="abs topbar-social"><i></i><i></i><i></i><i></i><i></i><i></i></div>

<!-- header -->
<div class="abs brand"><span class="brand-mark"></span><span class="brand-name">VLK</span></div>
<div class="abs brand-sub">VANTOLIREX CORPORATION</div>
<div class="abs callus">
  <svg width="5" height="8" viewBox="0 0 5 8"><rect x=".5" y=".5" width="4" height="7" rx=".8" fill="none" stroke="#888"/></svg>
  CALL US FREE: +1 555 010 2040
</div>
<div class="abs header-rule"></div>

<!-- navigation -->
<nav class="abs nav">
  <div class="abs nav-home">HOME<small>go to home</small></div>
  <div class="abs nav-item" style="left:150px">ABOUT</div>
  <div class="abs nav-sep" style="left:196px"></div>
  <div class="abs nav-item" style="left:214px">VLK&nbsp; DIVISIONS</div>
  <div class="abs nav-sep" style="left:292px"></div>
  <div class="abs nav-item" style="left:309px">PRODUCTS</div>
  <div class="abs nav-sep" style="left:368px"></div>
  <div class="abs nav-item" style="left:384px">SERVICES</div>
  <div class="abs nav-sep" style="left:432px"></div>
  <div class="abs nav-search">Search
    <svg width="7" height="7" viewBox="0 0 7 7"><circle cx="3" cy="3" r="2.2" fill="none" stroke="#aaa" stroke-width=".8"/><line x1="4.6" y1="4.6" x2="6.6" y2="6.6" stroke="#aaa" stroke-width=".8"/></svg>
  </div>
</nav>

<!-- hero -->
<section class="abs hero" role="img" aria-label="Photo of a hand holding a smartphone showing a payment app, coffee cup in the background"></section>
<h1 class="abs heading hero-title">Technology Solutions fOr National<br>Defense &amp; global Securiy</h1>
<p class="abs heading hero-sub">Connect and give them the help they want.</p>
<a class="abs btn btn-how">How It Works?</a>
<a class="abs btn btn-more">Read More</a>
<div class="abs hero-dots"><i></i><i></i><i></i><i></i></div>

<!-- features -->
<div class="abs feature" style="left:74px">
  <div class="feature-icon">
  <svg width="34" height="38" viewBox="0 0 34 38">
    <rect x="1" y="1" width="32" height="7" rx="1.5" fill="var(--blue)"/>
    <rect x="1" y="10" width="32" height="7" rx="1.5" fill="var(--blue)"/>
    <rect x="1" y="19" width="32" height="7" rx="1.5" fill="var(--blue)"/>
    <rect x="1" y="28" width="32" height="4" rx="1.5" fill="var(--blue)"/>
    <circle cx="28" cy="4.5" r="1" fill="#fff"/><circle cx="28" cy="13.5" r="1" fill="#fff"/><circle cx="28" cy="22.5" r="1" fill="#fff"/>
    <line x1="17" y1="32" x2="17" y2="37" stroke="var(--blue)" stroke-width="1.5"/>
    <circle cx="17" cy="36" r="2" fill="var(--blue)"/>
  </svg>
  </div>
  <h3>Communication &amp; Networking</h3>
  <p>Are many variations of passages of Lorem Ipsum available, but the majority have suffered altera-tion some form, by injected humour, or ran-domised words which don't look even slightly</p>
</div>
<div class="abs feature" style="left:299px">
  <div class="feature-icon">
  <svg width="38" height="38" viewBox="0 0 38 38" fill="none" stroke="var(--blue)" stroke-width="1.2">
    <circle cx="4" cy="4" r="2.5"/><circle cx="34" cy="4" r="2.5"/><circle cx="6" cy="34" r="2.5"/><circle cx="34" cy="34" r="2.5"/>
    <circle cx="19" cy="18" r="4"/>
    <line x1="6" y1="6" x2="16" y2="15"/><line x1="32" y1="6" x2="22" y2="15"/><line x1="8" y1="32" x2="16" y2="22"/><line x1="32" y1="32" x2="22" y2="22"/>
  </svg>
  </div>
  <h3>Technology Inserstion</h3>
  <p>Are many variations of passages of Lorem Ipsum available, but the majority have suffered alteration some form, by injected humour, or randomised words which don't look even slightly believable. If</p>
</div>
<div class="abs feature" style="left:527px">
  <div class="feature-icon">
  <svg width="38" height="32" viewBox="0 0 38 32">
    <path d="M9 26a7 7 0 0 1-1-13.9A10 10 0 0 1 27 9a8 8 0 0 1 2 17z" fill="var(--blue)"/>
    <circle cx="22" cy="22" r="5" fill="#fff"/><circle cx="22" cy="22" r="3" fill="var(--blue)"/>
    <circle cx="30" cy="26" r="3.5" fill="#fff"/><circle cx="30" cy="26" r="2" fill="var(--blue)"/>
  </svg>
  </div>
  <h3>Cloud Solutions</h3>
  <p>Are many variations of passages of Lorem Ipsum available, but the majority have suffered altera-tion some form, by injected humour, or ran-domised words which don't look even slightly</p>
</div>
<div class="abs features-rule"></div>

<!-- testimonial -->
<section class="abs testimonial"></section>
<div class="abs avatar" role="img" aria-label="Portrait photo of the company CEO"></div>
<div class="abs arrow-box" style="left:72px"><svg width="5" height="6" viewBox="0 0 5 6"><path d="M4 0L1 3l3 3" fill="none" stroke="#fff"/></svg></div>
<div class="abs arrow-box" style="left:632px"><svg width="5" height="6" viewBox="0 0 5 6"><path d="M1 0l3 3-3 3" fill="none" stroke="#fff"/></svg></div>
<blockquote class="abs quote">&#8220; In enim justo, rhoncus ut, imperdiet a, venenatis vitae, justo. Nullam dictum felis eu pede mollis pretium. Integer tincidunt. Cras dapibus. Vivamus elementum semper nisi. Aenean vulputate eleifend tellus. &#8221;</blockquote>
<p class="abs quote-author">Daniel Marsh - CEO</p>

<!-- about -->
<h2 class="abs section-title about-title">
  <svg width="12" height="9" viewBox="0 0 12 9"><path d="M1 8l3-4 3 2 4-5" fill="none" stroke="var(--blue-soft)" stroke-width="1.3"/></svg>
  About Vantolirex (VLK)
</h2>
<div class="abs about-rule"></div>
<p class="abs about-intro">Nam quam nunc, blandit vel, luctus pulvinar, hendrerit id, lorem. Maecenas nec odio et ante tincidunt tempus. Donec vitae sapien ut libero venenatis faucibus. Nullam quis ante. Etiam sit amet orci eget eros faucibus tincidunt.</p>
<ul class="abs about-list">
  <li><span class="ico"></span>Are many variations of passages of Lorem Ipsum available, but the majority have suffered Alteration some<span class="plus">+</span></li>
  <li><span class="ico"></span>form, by injected humour, or randomised words which don't look evenSlightly Believable. If you are going to<span class="plus">+</span></li>
  <li><span class="ico"></span>use a passage of Lorem Ipsum, you need to be sure there isn't Snything embarrassing hidden in the middle of<span class="plus">+</span></li>
  <li><span class="ico"></span>text. All the Lorem Ipsum generators on the Internet tend to repeat predefined chunks as necessary, making<span class="plus">+</span></li>
  <li><span class="ico"></span>this the first true generator on the Interne<span class="plus">+</span></li>
</ul>

<!-- news -->
<h2 class="abs section-title news-title">
  <svg width="8" height="10" viewBox="0 0 8 10"><path d="M.5.5h5l2 2v7H.5z" fill="none" stroke="var(--blue-soft)"/></svg>
  Latest News
</h2>
<div class="abs news-arrows"><i></i><i></i></div>
<div class="abs news-image" role="img" aria-label="Illustration of game controllers and gadgets above a monitor"></div>
<div class="abs news-date">March 1, 2012</div>
<p class="abs news-type">Link Post Type</p>
<p class="abs news-text">Vestibulum ante ipsum primis in faucibus orci luctus et ultrices posuere cubilia Curae; In ac dui quis mi consectetuer lacinia. Nam pretium turpis et arcu. Duis arcu tortor, suscipit eget, imperdiet nec, imperdiet iaculis, ipsum.</p>

<!-- call to action -->
<section class="abs cta"></section>
<h2 class="abs heading cta-title">How&nbsp; Does <em>Vantolirex Solution</em> Help People</h2>
<p class="abs cta-text">Lorem ipsum dolor sit amet, consectetur adipiscing elit. Morbi sodales vehicula odio quis lobortis. Aenean lacinia pulvin&nbsp; Aenean lacinia pulvinar hendrerit.</p>
<a class="abs btn btn-cta">Read More</a>

<!-- partners -->
<h2 class="abs heading partners-title">Our Partners</h2>
<div class="abs partner" style="left:92px;top:996px;width:76px;height:18px;background:#3a3a3a;border-radius:2px" aria-label="Partner badge"></div>
<div class="abs partner" style="left:263px;top:978px;width:54px;height:54px;background:#ee8a3c;border-radius:50%" aria-label="Partner badge"></div>
<div class="abs partner" style="left:392px;top:990px;width:96px;height:28px;background:#3c5fa8;border-radius:2px" aria-label="Partner badge"></div>
<div class="abs partner" style="left:588px;top:976px;width:66px;height:46px;background:#4ba6a4;border-radius:2px" aria-label="Partner badge"></div>

<!-- footer -->
<footer class="abs footer"></footer>
<div class="abs footer-brand"><span class="brand-mark"></span><span class="brand-name">VLK</span></div>
<div class="abs footer-sub">VANTOLIREX CORPORATION</div>
<p class="abs footer-text">Lorem ipsum dolor sit amet, consectetuer adipiscing elit, sed diam nonummy nibh euismod tincidunt ut laoreet dolore magna aliquam erat volutpat.</p>
<h3 class="abs newsletter-title">Join Our Newsletter</h3>
<p class="abs newsletter-text">Stay up to date with the latest news by subscribing to our newsletter.</p>
<div class="abs newsletter-input">Your E-mail Here...</div>
<a class="abs btn newsletter-btn">Subscribe</a>
<div class="abs bottombar"></div>
<p class="abs copyright">Copyrights © 2014 Vantolirex.com - All Rights Reserved</p>
<div class="abs bottom-social"><i></i><i></i><i></i><i></i><i></i></div>

</body>
</html>
```